CASH PAYMENT DISCOUNT NOTICE POSTED IN CASH REGISTER AREA

LOOKING TO MAKE A FLYER OR A POSTED NOTICE FOR CUSTOMERS PAYING FOR OVER-THE-COUNTER MERCHANDISE AND WHO PAY BY CASH METHOD TO GET A 4% CASH DISCOUNT.
PRESCRIPTIONS ARE EXCLUDED FROM THIS CASH DISCOUNT.

Target Market(s)

RETAIL CUSTOMERS

Industry/Entity Type

RETAIL PHARMACY

Colors
0054AA
0677BA
7BADD7
CADEEF
E8F1F8
EB3D1F
EC4F4E
F09395
F8D3D4
FCEDEE

Requirements
Must have
• LOGO COLORS
Nice to have
• EYE CATCHING

```html
<!DOCTYPE html>
<html lang="en">
<head>
<meta charset="utf-8">
<title>Cash Discount Notice</title>
<link href="https://fonts.googleapis.com/css2?family=Lato:wght@400;700;900&display=swap" rel="stylesheet">
<style>
  :root {
    --page-bg: #ccd6e8;
    --paper: #ffffff;
    --brand-blue: #0054aa;
    --sky-blue: #2b9ce6;
    --mid-blue: #0677ba;
    --brand-red: #b3202a;
    --ink: #1c1c1c;
    --photo-a: #e8f1f8;
    --photo-b: #cadeef;
  }
  html, body {
    margin: 0;
    width: 1200px;
    height: 1200px;
    overflow: hidden;
    background: var(--page-bg);
    font-family: "Lato", sans-serif;
  }
  .flyer {
    position: absolute;
    left: 245px;
    top: 122px;
    width: 741px;
    height: 961px;
    background: var(--paper);
    box-shadow: 0 4px 14px rgba(0,0,0,0.18);
    overflow: hidden;
  }
  .flyer-art {
    position: absolute;
    inset: 0;
    width: 741px;
    height: 961px;
  }
  .badge-text {
    position: absolute;
    left: 440px;
    top: 205px;
    width: 282px;
    text-align: center;
    color: #fff;
    font-weight: 900;
    line-height: 1;
  }
  .badge-text .percent { display: block; font-size: 104px; letter-spacing: -1px; }
  .badge-text .label { display: block; font-size: 34px; margin-top: 2px; }
  .offer {
    position: absolute;
    left: 100px;
    top: 608px;
    width: 676px;
    text-align: center;
    color: var(--ink);
  }
  .offer .lead {
    margin: 0;
    font-weight: 700;
    font-size: 29px;
    line-height: 1.3;
  }
  .offer .method {
    display: inline-block;
    margin: 2px 0 0;
    font-weight: 900;
    font-size: 45px;
    color: var(--brand-blue);
    border-bottom: 3px solid var(--brand-red);
    padding: 0 4px 2px;
    line-height: 1.1;
  }
  .offer .note {
    margin: 14px 0 0;
    font-size: 20px;
    font-weight: 400;
  }
  .brand {
    position: absolute;
    left: 120px;
    top: 835px;
    width: 636px;
    display: flex;
    align-items: center;
    justify-content: center;
    gap: 18px;
  }
  .brand-dot {
    width: 44px;
    height: 44px;
    border-radius: 50%;
    background: var(--brand-blue);
  }
  .brand-name {
    font-weight: 700;
    font-size: 44px;
    color: var(--brand-blue);
  }
</style>
</head>
<body>
<main class="flyer">
  <svg class="flyer-art" viewBox="0 0 741 961" xmlns="http://www.w3.org/2000/svg">
    <defs>
      <linearGradient id="photoFill" x1="0" y1="0" x2="1" y2="1">
        <stop offset="0" stop-color="#e8f1f8"/>
        <stop offset="1" stop-color="#cadeef"/>
      </linearGradient>
    </defs>
    <path class="corner-band" d="M640 0 H741 V340 C690 260 650 160 640 0 Z" fill="var(--brand-blue)"/>

    <g class="swoosh">
      <path class="swoosh-outer" d="M330 424 C170 450 30 560 0 800 V330 Z" fill="var(--brand-blue)"/>
      <path class="swoosh-light" d="M330 424 C180 445 40 530 0 720 V330 Z" fill="var(--sky-blue)"/>
      <path class="swoosh-red" d="M330 424 C195 440 55 505 0 650 V330 Z" fill="var(--brand-red)"/>
      <path class="swoosh-light-inner" d="M330 424 C210 435 70 485 0 590 V330 Z" fill="var(--sky-blue)"/>
      <path class="swoosh-top" d="M330 424 C225 430 80 465 0 540 V330 Z" fill="var(--brand-blue)"/>
    </g>

    <path class="pharmacy-photo" role="img" aria-label="Photo: smiling pharmacist at a pharmacy counter with shelves of medicine behind"
          d="M0 0 H640 C648 160 690 250 741 305 V330 C600 330 470 400 330 424 C200 440 90 410 0 350 Z"
          fill="url(#photoFill)" stroke="#fff" stroke-width="6"/>
    <circle class="discount-badge" cx="581" cy="314" r="143" fill="var(--brand-red)" stroke="#fff" stroke-width="9"/>
    <circle class="cash-badge" cx="411" cy="462" r="112" fill="var(--sky-blue)" stroke="#fff" stroke-width="9"/>
    <g class="cash-icon" fill="none" stroke="#fff" stroke-width="6" stroke-linejoin="round">
      <rect x="361" y="431" width="100" height="62" rx="4" transform="rotate(-30 411 462)"/>
      <circle cx="411" cy="462" r="14"/>
    </g>
  </svg>

  <div class="badge-text">
    <span class="percent">4%</span>
    <span class="label">CASH</span>
    <span class="label">DISCOUNT</span>
  </div>

  <section class="offer">
    <p class="lead">FOR CUSTOMERS PAYING FOR<br>OVER-THE-COUNTER MERCHANDISE</p>
    <p class="method">BY CASH METHOD</p>
    <p class="note">*Prescriptions are excluded from this cash discount.</p>
  </section>

  <footer class="brand">
    <span class="brand-dot"></span>
    <span class="brand-name">Marlow Pharmacy</span>
  </footer>
</main>
</body>
</html>
```